Business Card Design Project

We need a business card design for a new company based in Singapore called 'Bright Ladder Pte Ltd'. We provide personal development training and emotional intelligence workshops. Our slogan is "Actualize your potentials". We will not have a company address on the business card. Only phone number, email address and website address.

Target Market(s)

Adults age 25 to 45 years old.
Mostly working in a job.

Industry/Entity Type

Training

Colors
0255a2
f37123

```html
<!DOCTYPE html>
<html lang="en">
<head>
<meta charset="utf-8">
<title>Bright Ladder Pte Ltd – Business Card</title>
<link rel="stylesheet" href="https://fonts.googleapis.com/css2?family=Roboto:wght@300;700&display=swap">
<style>
  :root {
    --stage: #000000;
    --front-bg: #f0fdfe;
    --back-bg: #001a66;
    --brand-blue: #0255a2;
    --brand-navy: #0b2a6e;
    --slogan-light: #7e8dc0;
    --rule: #8e96a8;
    --contact-text: #9aa6cc;
    --back-slogan: #d2d9f0;
    --mark-faint: #0e2a78;
  }
  html, body {
    margin: 0;
    padding: 0;
    width: 1200px;
    height: 447px;
    overflow: hidden;
    background: var(--stage);
    font-family: "Roboto", Arial, sans-serif;
  }
  .canvas {
    position: relative;
    width: 1200px;
    height: 447px;
  }
  .card-front, .card-back {
    position: absolute;
    top: 68px;
    height: 310px;
    width: 530px;
    overflow: hidden;
  }
  .card-front { left: 70px; background: var(--front-bg); }
  .card-back { left: 600px; background: var(--back-bg); }

  .brand {
    position: absolute;
    left: 170px;
    top: 118px;
    display: flex;
    align-items: center;
    gap: 10px;
  }
  .brand-dot {
    width: 40px;
    height: 40px;
    border-radius: 50%;
    background: var(--brand-blue);
  }
  .brand-name {
    font-weight: 700;
    font-size: 19px;
    color: var(--brand-navy);
    white-space: nowrap;
  }
  .front-slogan {
    position: absolute;
    right: 172px;
    top: 216px;
    margin: 0;
    text-align: right;
    font-weight: 300;
    font-size: 20px;
    line-height: 20px;
    color: var(--slogan-light);
  }
  .front-rule {
    position: absolute;
    left: 226px;
    right: 0;
    top: 259px;
    height: 1px;
    background: var(--rule);
  }

  .back-mark {
    position: absolute;
    left: 6px;
    top: 80px;
  }
  .contact {
    position: absolute;
    right: 35px;
    top: 172px;
    margin: 0;
    text-align: right;
    font-weight: 300;
    font-size: 13px;
    line-height: 18px;
    color: var(--contact-text);
  }
  .back-slogan {
    position: absolute;
    right: 35px;
    top: 235px;
    margin: 0;
    font-weight: 300;
    font-size: 20px;
    color: var(--back-slogan);
  }
</style>
</head>
<body>
<div class="canvas">
  <section class="card-front">
    <div class="brand">
      <span class="brand-dot"></span>
      <span class="brand-name">Bright Ladder Pte Ltd</span>
    </div>
    <p class="front-slogan">Actualize<br>Your Potentials</p>
    <div class="front-rule"></div>
  </section>

  <section class="card-back">
    <svg class="back-mark" width="260" height="260" viewBox="0 0 260 260" aria-hidden="true">
      <circle cx="130" cy="130" r="120" fill="none" stroke="var(--mark-faint)" stroke-width="14"/>
    </svg>
    <p class="contact">
      Ph. 010 220 003 300<br>
      e-mail : info@brightladder.com<br>
      web : www.brightladder.com
    </p>
    <p class="back-slogan">Actualize Your Potentials</p>
  </section>
</div>
</body>
</html>
```